Design a powerpoint background using company logo/colours

We require a powerpoint background that incorporates our company colours and logo. I have attached the logo in various sizes.

Have fun and be imaginative

Our company colours are white and Red-236, Green-22 and Blue 86.
Please use these colours in designing the ppt background

Industry/Entity Type

It Company

Colors

Designer to choose colors to be used in the design.

```html
<!DOCTYPE html>
<html lang="en">
<head>
<meta charset="utf-8">
<title>Nexora Slide Template</title>
<link rel="stylesheet" href="https://fonts.googleapis.com/css2?family=Arimo:wght@400;700&display=swap">
<style>
  :root {
    --brand: #ec1656;
    --white: #ffffff;
    --ink: #333333;
    --ink-soft: #3a3a3a;
    --wash-top: #e8e9ea;
    --wash-bottom: #ffffff;
    --sky-top: #2f5fae;
    --sky-bottom: #5b8fd8;
  }
  * { margin: 0; padding: 0; box-sizing: border-box; }
  html, body { width: 1200px; height: 900px; overflow: hidden; background: var(--white); }
  body { font-family: "Arimo", Arial, sans-serif; color: var(--ink); }

  .slide { position: relative; width: 1200px; height: 900px; overflow: hidden; }

  .top-band { position: absolute; left: 0; top: 0; width: 100%; height: 30px; background: var(--brand); }

  .header { position: absolute; left: 0; top: 30px; width: 100%; height: 130px; background: var(--white); }
  .brand { position: absolute; left: 46px; top: 28px; display: flex; align-items: center; gap: 14px; }
  .brand-name { font-size: 62px; font-weight: 700; color: var(--brand); line-height: 1; letter-spacing: -1px; }
  .brand-mark { width: 46px; height: 46px; border: 3px solid var(--brand); border-radius: 50%; }
  .meta { position: absolute; right: 44px; top: 26px; text-align: right; font-size: 17px; line-height: 20px; color: var(--ink); text-transform: uppercase; }

  .stage { position: absolute; left: 0; top: 160px; width: 100%; height: 680px;
           background: linear-gradient(180deg, var(--wash-top) 0%, #f3f4f5 55%, var(--wash-bottom) 100%); }

  .content { position: absolute; left: 88px; top: 68px; width: 620px; }
  .heading { font-size: 43px; font-weight: 400; color: var(--brand); line-height: 1; margin-bottom: 11px; margin-left: -2px; }
  .body-text { font-size: 15px; line-height: 19.5px; color: var(--ink-soft); }
  .body-text + .body-text { margin-top: 19.5px; }
  .body-text.spaced { margin-top: 52px; }

  .feature-photo { position: absolute; left: 780px; top: 72px; width: 376px; height: 374px; border-radius: 10px;
                   background: linear-gradient(180deg, var(--sky-top) 0%, var(--sky-bottom) 100%); }

  .footer { position: absolute; left: 0; top: 840px; width: 100%; height: 29px; background: var(--brand);
            color: var(--white); font-size: 13px; }
  .footer-copy { position: absolute; left: 46px; top: 7px; }
  .footer-presenter { position: absolute; left: 323px; top: 7px; }
  .footer-divider { position: absolute; left: 297px; top: 840px; width: 1px; height: 60px; background: var(--brand); }
  .footer-divider::after { content: ""; position: absolute; left: 0; top: 0; width: 1px; height: 29px; background: var(--white); }
  .page-number { position: absolute; left: 1122px; top: 838px; width: 34px; height: 32px; background: var(--white);
                 border: 1px solid var(--brand); color: var(--brand); font-size: 16px; text-align: center; line-height: 30px; }
</style>
</head>
<body>
<div class="slide">
  <div class="top-band"></div>

  <header class="header">
    <div class="brand">
      <span class="brand-name">nexora</span>
      <span class="brand-mark"></span>
    </div>
    <div class="meta">
      <div class="meta-title">Presentation Title</div>
      <div class="meta-date">Date</div>
    </div>
  </header>

  <main class="stage">
    <section class="content">
      <h1 class="heading">Heading</h1>
      <p class="body-text">Lorem Ipsum is simply dummy text of the printing and typesetting industry.<br>
      Lorem Ipsum has been the industry's standard dummy text ever since the 1500s, when an unknown printer took a galley of type and scrambled it to make a type specimen book. It has survived not only five centuries, but also the leap into electronic typesetting, remaining essentially unchanged.</p>
      <p class="body-text spaced">Lorem Ipsum is simply dummy text of the printing and typesetting industry.<br>
      Lorem Ipsum has been the industry's standard dummy text ever since the 1500s, when an unknown printer took a galley of type and scrambled it to make a type specimen book. It has survived not only five centuries, but also the leap into electronic typesetting, remaining essentially unchanged standard dummy text ever since the 1500s, when an unknown printer took a galley of type and scrambled it to make a type specimen book. It has survived not only five centuries, but also the leap into electronic typesetting, remaining essentially unchanged.</p>
      <p class="body-text">Dummy text ever since the 1500s, when an unknown printer took a galley of type and scrambled it to make a type specimen book. It has survived not only five centuries, but also the leap into electronic typesetting, remaining essentially unchanged.</p>
    </section>

    <div class="feature-photo" role="img" aria-label="Photo of a telecommunications lattice tower with microwave dish antennas against a blue sky"></div>
  </main>

  <footer class="footer">
    <span class="footer-copy">Copyright © 2014 Nexora Group Pty Ltd</span>
    <span class="footer-presenter">Presenting by ANIKA RAO</span>
  </footer>
  <div class="footer-divider"></div>
  <div class="page-number">2</div>
</div>
</body>
</html>
```